Business Card Design

We need a design that will also transfer to car decals
We need a design that will speak to the average person needing home and office remodeling
The design should be fresh, exciting, easy to read in a glance and unique
We would like a die-cut tool belt
Bright colors and evenly spaced information

Target Market(s)

Home and business owners
Middle and Upper Income property owners
Families and people with fixer upper homes

Industry/Entity Type

Business

Contact Information for Business Card

Looking for the best Bay Area Handyman? Here I am!
RKW Handyman Services does it all at prices regular people can afford.
Electrical, Plumbing, Carpentry, Remodeling, Fencing, Picture and window placement, Hauling ... and anything else you can imagine!
510-374-2196
Serving the Entire Bay Area
Free Estimates! Call us Today to turn your dreams into reality!

Font styles to use
Serif

Requirements
Must have
• Speaks to the average person
stands out among similar industry cards
Nice to have
• fun, comical, you want to hold on to this card
Should not have
• bland colors
look too crowded

```html
<!DOCTYPE html>
<html lang="en">
<head>
<meta charset="utf-8">
<title>RKW Handyman Services – Business Card</title>
<link rel="stylesheet" href="https://fonts.googleapis.com/css2?family=Tinos&display=swap">
<style>
  :root {
    --stage-light: #ffffff;
    --stage-dark: #dcdddf;
    --card-blue-light: #1a86d6;
    --card-blue: #0a72c4;
    --card-blue-deep: #0062b0;
    --card-white: #ffffff;
    --text-white: #ffffff;
    --text-gray: #6d6e71;
    --text-red: #be1e2d;
  }
  * { margin: 0; padding: 0; box-sizing: border-box; }
  html, body {
    width: 1200px;
    height: 1200px;
    overflow: hidden;
  }
  body {
    position: relative;
    background: radial-gradient(circle at 50% 50%, var(--stage-light) 0%, var(--stage-light) 30%, var(--stage-dark) 100%);
    font-family: "Tinos", "Times New Roman", serif;
  }
  .card {
    position: absolute;
    left: 227px;
    width: 745px;
    height: 435px;
    text-align: center;
  }
  .card-front {
    top: 83px;
    background: radial-gradient(ellipse at 50% 45%, var(--card-blue-light) 0%, var(--card-blue) 55%, var(--card-blue-deep) 100%);
    color: var(--text-white);
  }
  .card-back {
    top: 608px;
    background: var(--card-white);
    color: var(--text-gray);
  }
  .line {
    position: absolute;
    left: 0;
    right: 0;
    line-height: 1;
    white-space: nowrap;
  }
  .phone       { top: 18px;  font-size: 58px; }
  .call-to-act { top: 133px; font-size: 33px; }
  .estimates   { top: 196px; font-size: 64px; }
  .service-area{ top: 286px; font-size: 50px; }

  .headline    { top: 30px;  font-size: 35px; }
  .greeting    { top: 94px;  font-size: 44px; color: var(--text-red); }
  .pitch       { top: 170px; font-size: 27px; }
  .pitch-cont  { top: 215px; font-size: 27px; }
  .services    { font-size: 27px; color: var(--text-red); }
  .services-1  { top: 257px; }
  .services-2  { top: 302px; }
  .closing     { top: 346px; font-size: 27px; }
</style>
</head>
<body>
  <section class="card card-front" aria-label="Business card front">
    <p class="line phone">510-374-2196</p>
    <p class="line call-to-act">Call us Today to turn your dreams into reality!</p>
    <p class="line estimates">Free Estimates</p>
    <p class="line service-area">“Serving the Entire Bay Area”</p>
  </section>

  <section class="card card-back" aria-label="Business card back">
    <p class="line headline">Looking for the best Bay Area Handyman?</p>
    <p class="line greeting">Here I am!</p>
    <p class="line pitch">RKW Handyman Services does it all at prices regular people</p>
    <p class="line pitch-cont">can afford.</p>
    <p class="line services services-1">Electrical, Plumbing, Carpentry, Remodeling, Fencing,</p>
    <p class="line services services-2">Picture and window placement, Hauling...</p>
    <p class="line closing">and anything else you can imagine!</p>
  </section>
</body>
</html>
```